Dynamic Website Design For Dynamic Speaker and Business Coach!

Professional Website Design for a for a Professional Business coach, Business trainer, and Speaker.

Note: This is for design only. No coding required. We want to see your ideas for a great website! This will be a FUN design and not boring like others you may work on.

Please let your creative ideas flow. We have given you a ton of info along with videos to help you understand what we are after, however we WANT your creativity to shine through in your designs!

We are a professional company that has run hundreds of crowdsourced projects on multiple platforms. If you participate in this contest (we hope you do) you can expect great video feedback, consistent feedback, and also our guarantee that if we know your website design will not be what we are looking for we will notify you so you don’t waste your time if there is no chance of you winning.

We respect and recognize this is how you make your living and we will not play games. We look forward to an awesome contest and awesome website designs.

Design Brief:

We are looking for a fresh and fun new design for

http://www.brightpath-advisory.net

This individual (Dana Holloway) teaches and trains corporations and businesses in the fields of leadership, sales, communication, business operations etc. Additionally this business teaches and mentors business professionals in a small group level or 1 on 1.

The website needs to convey trust, professionalism, and affluent, while at the same time having some personality!

This business operates on 3 core principles that we would like to see incorporated into the logo if it is a good fit. The 3 principals are:

Focus
Accountability
Results

Here is a video to help explain what we like about the current site and what we don’t like:
http://clipvault.example/t/QwpLmr82kTnb

As you can see the website is geared towards business professionals. Please look over the website to learn what they do. Obviously this is not a good website so we need your help.

We want a website that is professional-looking, has personality and is geared more towards promoting Dana Holloway, the owner of Summit Path Advisory as a Speaker and Business Consultant. The more you can incorporate clean, professional and fun personality elements into the design, the better off you are at winning.

Here are some examples of other sites in their business that have some things we like:

http://velvetcompass.com Please watch video to learn what we like and don’t like:
http://clipvault.example/t/NrtHq7YpLwc

http://tallpinegrowth.com Please watch video to learn what we like and don’t like:
http://clipvault.example/t/J8vDkrWa

http://www.marthaquince.com Please watch video to learn what we like and don’t like:
http://clipvault.example/t/Pz3mx9Rb2Kq

http://www.vantix7.com Please watch video to learn what we like and don’t like:
http://clipvault.example/t/7Gwe4sNhydv

NOTE: We do not want to copy anything outright. We want to learn, model and take their ideas and make them better. We also want to be flexible and take what we like along with your creativity to make an amazing design.

Here is what we are looking for in more specific terms:

Colors: We like the darker blue (not the light blue like the site) and also a burnt orange. I’ve attached her Logo so you can get an idea and feel for the colors.

When looking at colors please know that the current site and look is NOT what we are going for. We are going for a clean and professional look but also a look that is BOLD, FUN, and Vibrant (hence the colors).

Menu: Horizontal. We like bold and easy to read menu items. Don’t make it small and cluttered.

Site Structure: Clean and easy to navigate. We have a lot of content to display so we need a clean structure that breaks up the text and content areas.
Images: Please pull images from the current site. We can always replace the images of course, but if you show them “their own stuff” in the new design you will be closer to winning because it will feel more like “them”

Look and Feel: Professional. Fun. High-End. Business-like. This website needs to convey that Dana Holloway and Summit Path Advisory are professional. That Dana Holloway is a sought-after Speaker and Business Consultant who knows what she is talking about; can be serious when she needs to be, but also likes to have fun with her clients. This site must convey that!

Content Areas: It is a safe bet that if it is on the current site we need it on the new site. So don’t drop anything as it makes it hard to “cut content”.

What we don't want: We do not want clutter, boring, or templates or themes. We don’t want too cartoony, too cute, or too fancy… Be creative!

Out of respect to professional designers who really are working hard to win if you do not follow this brief, you submit worn out themes, templates, or boring designs you will be eliminated. We are offering great prize money for this so we expect great visual designs.
Updates

Project Deadline Extended
Reason: Our client is out of town, and waiting to hear feedback from them. So, in the meantime, we wanted to keep the project going to see what else you designers can come up with. As soon as we hear back from our client, we will pass along the info. Thanks!

Target Market(s)

Target Audience is entrepreneurs and business professionals alike. This is all business to business stuff.

This person teaches and trains startups and billion dollar companies. The common thread is that they are all businesses and companies who need help in various areas including sales, communication, business operations, etc.

Industry/Entity Type

Business

Font styles to use
Sans Serif

Requirements
Must have
• Brief is very detailed. Please review
Nice to have
Should not have

```html
<!DOCTYPE html>
<html lang="en">
<head>
<meta charset="utf-8">
<title>Summit Path Advisory</title>
<link href="https://fonts.googleapis.com/css2?family=Open+Sans:wght@400;600;700&display=swap" rel="stylesheet">
<style>
:root{
  --orange:#e07a2f;
  --blue:#1a7cc1;
  --navy:#23307a;
  --text:#5f5f5f;
  --dark:#1e1e1e;
  --bg:#f6f6f6;
  --line:#e2e2e2;
}
*{margin:0;padding:0;box-sizing:border-box}
html,body{width:1200px;height:1196px;overflow:hidden}
body{font-family:'Open Sans',Arial,sans-serif;background:var(--bg);color:var(--text);position:relative}
.abs{position:absolute}
.brand{left:233px;top:20px;display:flex;align-items:center;gap:10px}
.brand-dot{width:38px;height:38px;border-radius:50%;background:var(--blue)}
.brand-name{font-size:22px;font-weight:700;color:var(--navy);line-height:1}
.phone{left:617px;top:26px;font-size:18px;color:var(--blue)}
.social{left:754px;top:29px;display:flex;gap:4px}
.social span{width:18px;height:18px;border-radius:50%;background:var(--navy)}
.social span:nth-child(2){background:#2aa3e0}
.social span:nth-child(3){background:#1a6fa6}
.social span:nth-child(4){background:#d93a2b}
.search{left:855px;top:28px;width:111px;height:19px;border:1px solid #cfcfcf;border-radius:10px;background:#fff;font-size:9px;color:#888;padding:3px 8px}
.search svg{position:absolute;right:6px;top:4px}
.nav{left:233px;top:84px;width:733px;height:27px;border-bottom:1px solid var(--line);display:flex;justify-content:space-between;padding:0 13px;font-size:10px;color:#444;text-transform:uppercase;white-space:nowrap}
.nav a{color:inherit;text-decoration:none;height:27px;padding-top:2px}
.nav a.active{color:var(--orange);border-bottom:1px solid var(--orange)}
.hero-title{left:233px;top:131px;width:340px;font-size:22.5px;line-height:26px;color:var(--orange);letter-spacing:.8px}
.hero-sub{left:233px;top:197px;width:330px;font-size:13px;line-height:17px;color:var(--blue)}
.hero-copy{left:233px;top:243px;width:330px;font-size:9.8px;line-height:17px}
.btn{top:326px;height:27px;padding:0 9px;font-size:11px;font-weight:600;color:#fff;line-height:26px;border-radius:2px;white-space:nowrap}
.btn-blue{left:233px;background:var(--blue);border-bottom:2px solid #0f5a92}
.btn-orange{left:390px;background:var(--orange);border-bottom:2px solid #b35a1c}
.video{overflow:hidden}
.play{position:absolute;left:50%;top:50%;transform:translate(-50%,-50%)}
.hero-video{left:579px;top:130px;width:387px;height:243px;background:linear-gradient(180deg,#3e8aa6,#1e5d78)}
.band{left:0;top:403px;width:1200px;height:330px;background:#fff;border-top:1px solid var(--line);border-bottom:1px solid var(--line)}
.portrait{left:233px;top:372px;width:250px;height:360px;background:linear-gradient(180deg,#d9d2ca,#2b2e36 70%,#1f4fa0)}
.about-title{left:499px;top:425px;font-size:25px;color:var(--navy)}
.about-title span{color:var(--orange)}
.about-copy{left:498px;top:463px;width:468px;font-size:9.8px;line-height:16.7px}
.videos-title{left:498px;top:565px;font-size:17px;color:var(--orange)}
.thumb{top:595px;width:142px;height:99px;background:linear-gradient(180deg,#2f6278,#1b3f52)}
.more{left:498px;top:705px;font-size:9.5px;color:var(--blue)}
.col-title{top:767px;font-size:16.5px;color:var(--blue)}
.col-copy{top:799px;width:200px;font-size:9.8px;line-height:16.7px}
.read{top:906px;font-size:9.8px;font-weight:700;color:var(--orange)}
.arrows{left:943px;top:769px}
.testimonial{left:706px;top:798px;width:260px}
.quote{position:relative;width:260px;min-height:85px;background:var(--orange);color:#fff;font-size:9.3px;line-height:16.7px;padding:9px 8px 9px 32px}
.quote::before{content:"\201C";position:absolute;left:10px;top:0;font-size:30px;line-height:34px;color:rgba(255,255,255,.5);font-style:italic}
.quote::after{content:"";position:absolute;left:12px;bottom:-10px;border-left:10px solid var(--orange);border-bottom:10px solid transparent}
.author{margin-top:15px;margin-left:-1px;font-size:9.8px;color:#444}
.author span{color:var(--orange)}
.footer{left:0;top:950px;width:1200px;height:189px;background:var(--dark);color:#ddd}
.f-title{top:30px;font-size:12px;font-weight:600;color:#fff}
.f-list{top:58px;font-size:9.8px;line-height:20px;list-style:none}
.f-contact{left:562px;top:58px;font-size:9.8px;line-height:13.5px}
.f-contact em{font-style:normal;color:var(--orange)}
.signup{left:772px;top:28px;width:196px;font-size:10.3px;line-height:15px}
.signup b{color:#fff}
.signup .o{color:var(--orange)}
.field{top:105px;width:93px;height:23px;background:#2c2c2c;border:1px solid #3a3a3a;font-size:9.5px;color:#888;padding:4px 6px}
.submit{left:911px;top:139px;width:56px;height:24px;background:var(--orange);color:#fff;font-size:11px;font-weight:600;text-align:center;line-height:24px;border-radius:2px}
.copyright{left:234px;top:1160px;font-size:9.8px}
.badge{top:1155px;width:30px;height:26px}
</style>
</head>
<body>
<header>
  <div class="abs brand"><span class="brand-dot"></span><span class="brand-name">Summit Path Advisory</span></div>
  <div class="abs phone">(555) 014-2290</div>
  <div class="abs social"><span></span><span></span><span></span><span></span></div>
  <div class="abs search">Search...
    <svg width="9" height="9" viewBox="0 0 10 10"><circle cx="4" cy="4" r="3" fill="none" stroke="#777" stroke-width="1.4"/><line x1="6.3" y1="6.3" x2="9" y2="9" stroke="#777" stroke-width="1.4"/></svg>
  </div>
  <nav class="abs nav">
    <a class="active">Home</a><a>Passion</a><a>Who we are</a><a>Speaker</a><a>Free Videos</a><a>Web TV Show</a><a>Testimonials</a><a>Crestline Learning</a><a>Blog</a><a>Contact</a>
  </nav>
</header>

<section class="hero">
  <h1 class="abs hero-title" style="font-weight:400">Do you need More Focus, Accountability &amp; Result</h1>
  <p class="abs hero-sub">Are you searching to bridge the gap between where you are and where you want to be?</p>
  <p class="abs hero-copy">Dana Holloway is a results-based professional with over 25 years of experience in sales, marketing, facilitation, training and coaching. Committed to delivering more than expected by customers and clients. In 2008, opportunity knocked and she founded Summit Path Advisory.</p>
  <div class="abs btn btn-blue">Unplugged Web TV Show</div>
  <div class="abs btn btn-orange">Free Insider Videos</div>
  <div class="abs video hero-video" role="img" aria-label="Video still of Dana Holloway speaking, President/CEO">
    <svg class="play" width="60" height="60" viewBox="0 0 60 60"><circle cx="30" cy="30" r="28" fill="rgba(20,20,20,.75)" stroke="rgba(255,255,255,.35)" stroke-width="3"/><path d="M24 18 L42 30 L24 42Z" fill="#fff"/></svg>
  </div>
</section>

<section class="abs band"></section>
<div class="abs portrait" role="img" aria-label="Portrait of a businesswoman holding a blue clipboard"></div>
<h2 class="abs about-title" style="font-weight:400">About <span>Dana Holloway</span></h2>
<p class="abs about-copy">Integer a finibus libero, et gravida eros. Sed vel nisl at leo fermentum interdum. In tincidunt ex molestie, pharetra nibh tempus, porta nisl. Etiam scelerisque ipsum neque, sed efficitur purus facilisis vel. Nam egestas venenatis commodo. Fusce sit amet libero eu odio convallis fringilla rhoncus a nisl. Integer facilisis egestas neque, et finibus nisl viverra eget. Suspendisse feugiat suscipit varius. Morbi imperdiet sapien et luctus consectetur.</p>
<h3 class="abs videos-title" style="font-weight:400">Videos</h3>
<div class="abs video thumb" style="left:499px" role="img" aria-label="Video thumbnail of Dana Holloway"><svg class="play" width="40" height="40" viewBox="0 0 60 60"><circle cx="30" cy="30" r="28" fill="rgba(20,20,20,.7)" stroke="rgba(255,255,255,.35)" stroke-width="3"/><path d="M25 19 L41 30 L25 41Z" fill="#fff"/></svg></div>
<div class="abs video thumb" style="left:663px" role="img" aria-label="Video thumbnail of Dana Holloway"><svg class="play" width="40" height="40" viewBox="0 0 60 60"><circle cx="30" cy="30" r="28" fill="rgba(20,20,20,.7)" stroke="rgba(255,255,255,.35)" stroke-width="3"/><path d="M25 19 L41 30 L25 41Z" fill="#fff"/></svg></div>
<div class="abs video thumb" style="left:825px" role="img" aria-label="Video thumbnail of Dana Holloway"><svg class="play" width="40" height="40" viewBox="0 0 60 60"><circle cx="30" cy="30" r="28" fill="rgba(20,20,20,.7)" stroke="rgba(255,255,255,.35)" stroke-width="3"/><path d="M25 19 L41 30 L25 41Z" fill="#fff"/></svg></div>
<a class="abs more">View More Videos &gt;&gt;</a>

<section class="features">
  <h3 class="abs col-title" style="left:234px;font-weight:400">What we do</h3>
  <p class="abs col-copy" style="left:234px">Lorem ipsum dolor sit amet, consectetur adipiscing elit. Aenean luctus lectus erat, sit amet blandit nibh blandit eget. Sed sed sollicitudin nisl. Donec tempor malesuada egestas. Fusce pharetra interdum est eu condimentum.</p>
  <a class="abs read" style="left:234px">Read More +</a>
  <h3 class="abs col-title" style="left:469px;font-weight:400">Who we are</h3>
  <p class="abs col-copy" style="left:469px">Lorem ipsum dolor sit amet, consectetur adipiscing elit. Aenean luctus lectus erat, sit amet blandit nibh blandit eget. Sed sed sollicitudin nisl. Donec tempor malesuada egestas. Fusce pharetra interdum est eu condimentum.</p>
  <a class="abs read" style="left:469px">Read More +</a>
  <h3 class="abs col-title" style="left:706px;font-weight:400">Client’s Testimonials</h3>
  <svg class="abs arrows" width="24" height="16" viewBox="0 0 24 16"><path d="M9 2 L3 8 L9 14" fill="none" stroke="var(--blue)" stroke-width="2.5"/><path d="M15 2 L21 8 L15 14" fill="none" stroke="var(--blue)" stroke-width="2.5"/></svg>
  <div class="abs testimonial">
    <blockquote class="quote">Lorem ipsum dolor sit amet, consectetur adipiscing elit. Aenean luctus lectus erat, sit amet blandit nibh blandit eget. Sed sed sollicitudin nisl. Donec tempor malesuada egestas.</blockquote>
    <div class="author"><span>Mr. Alan Reed</span> (A Lorem Ipsum Co.)</div>
  </div>
</section>

<footer class="abs footer">
  <h4 class="abs f-title" style="left:235px">ABOUT US</h4>
  <ul class="abs f-list" style="left:234px"><li>Profile</li><li>Clients</li><li>Testimonials</li><li>Lectures by Dana Holloway</li></ul>
  <h4 class="abs f-title" style="left:414px">Programs</h4>
  <ul class="abs f-list" style="left:413px"><li>Public Programs</li><li>Inhouse Programs</li><li>School / Colleges</li><li>Positive Presenting</li></ul>
  <h4 class="abs f-title" style="left:563px">Contact Us</h4>
  <div class="abs f-contact">418 Larkspur Ave NE,<br>#212, Fairhaven,<br>New Mexico, 87000<br><span style="display:block;height:4px"></span><em>Phone :</em> (555) 014-2290<br><span style="display:block;height:4px"></span><em>Email :</em> info@brightpath-advisory.net</div>
  <div class="abs signup"><b>Change your thinking, change your results!</b> Sign up for my FREE report<br><span style="display:block;height:5px"></span><span class="o">Have Fun While Making Sales"</span> and make more money this month!</div>
  <div class="abs field" style="left:772px">Name</div>
  <div class="abs field" style="left:873px">Email</div>
  <div class="abs submit">Submit</div>
</footer>

<div class="abs copyright">©2014 Summit Path Advisory. All rights reserved</div>
<div class="abs badge" style="left:868px;border-radius:50%;background:#2f5b8f"></div>
<div class="abs badge" style="left:901px;border-radius:50%;background:#8a7a3a"></div>
<div class="abs badge" style="left:935px;background:#c2573a"></div>
</body>
</html>
```